Quellmont Haus National Website

We need a website to match our Logo. We will be selling american made vapeing Oils, batteries, Cartomizers, Clearomizers. We have a wharehouse location with couches, TVs streaming clipora, vending machine, and the worlds first flavor mixing bar. We have the lowest priced high grade oils. We will send pictures of the location. Relaxed atmoshpere and no lines for purchase. VIP cards for regulars.

(PLEASE KNOW THAT THE LOGO IS THE UPPER RIGHT LOGO ONLY OF THE FOUR ON THE FILE I ATTACHED)
Updates

Keep in mind we are are only looking for concept and a non coded website

Please know that we are looking for a non coded website

Industry/Entity Type

Purchase

Requirements
Must have
• Online cart, Blog,

```html
<!DOCTYPE html>
<html lang="en">
<head>
<meta charset="utf-8">
<title>Quellmont Haus — Vaping Oils &amp; Supplies</title>
<link rel="stylesheet" href="https://fonts.googleapis.com/css2?family=Open+Sans:wght@400;600;700;800&family=Oswald:wght@500;600&display=swap">
<style>
:root{
  --green:#8cc63e;
  --green-dark:#6fa52a;
  --black:#111;
  --ink:#222;
  --char:#2b2b2b;
  --grey:#e7e7e7;
  --grey-mid:#cfcfcf;
  --text:#555;
  --muted:#888;
  --white:#fff;
}
*{box-sizing:border-box;margin:0;padding:0}
html,body{width:870px;height:1200px;overflow:hidden}
body{font-family:"Open Sans",Arial,sans-serif;background:var(--white);color:var(--text);position:relative;font-size:8px}
a{color:inherit;text-decoration:none}
ul{list-style:none}

/* header */
.site-header{position:absolute;left:0;top:0;width:870px;height:58px;background:var(--white);border-bottom:1px solid var(--grey-mid)}
.brand{position:absolute;left:15px;top:12px;display:flex;align-items:center;gap:8px;font-family:"Open Sans",sans-serif;font-weight:700;font-size:26px;color:var(--char);letter-spacing:-.5px}
.brand-mark{width:10px;height:10px;background:var(--green)}
.main-nav{position:absolute;right:60px;top:10px;display:flex;gap:16px;font-size:8px;color:var(--char);font-weight:600}
.main-nav .active{border-bottom:2px solid var(--green);padding-bottom:2px}
.header-social{position:absolute;right:15px;top:9px;display:flex;gap:4px}
.header-social span{width:10px;height:10px;border-radius:50%;background:var(--char)}

/* tool bar */
.tool-bar{position:absolute;left:0;top:58px;width:870px;height:28px;background:var(--black)}
.shop-all{position:absolute;left:15px;top:0;width:90px;height:28px;background:var(--ink);color:var(--white);font-size:7.5px;font-weight:600;display:flex;align-items:center;gap:5px;padding-left:6px}
.shop-all svg{flex:none}
.search{position:absolute;left:208px;top:6px;display:flex;height:16px}
.search-scope{width:52px;background:var(--white);font-size:7px;color:var(--char);font-weight:700;padding:3px 5px;border-right:1px solid var(--grey-mid)}
.search-input{width:150px;background:var(--white);font-size:6.5px;color:var(--muted);padding:4px 5px}
.search-go{width:20px;background:var(--green);color:var(--white);font-size:7px;font-weight:700;text-align:center;padding-top:3px}
.account-links{position:absolute;left:640px;top:10px;font-size:7px;color:#bbb}
.cart{position:absolute;right:15px;top:5px;width:62px;height:18px;background:var(--green);color:var(--white);font-size:7.5px;font-weight:700;display:flex;align-items:center;gap:5px;padding-left:7px}

/* sidebar categories */
.category-menu{position:absolute;left:15px;top:86px;width:90px}
.category-menu li{height:25px;background:var(--black);border-bottom:1px solid #2e2e2e;color:var(--white);font-size:7.5px;font-weight:600;padding:7px 0 0 8px}
.category-menu li:first-child{background:var(--ink)}

/* hero */
.hero{position:absolute;left:105px;top:86px;width:750px;height:375px;background:linear-gradient(180deg,#f4f4f4,#e2e2e2)}
.hero-visual{position:absolute;left:70px;top:80px;width:330px;height:140px;border-radius:60px;background:radial-gradient(ellipse at 50% 50%,#c9cdd0 0%,#9aa1a6 45%,rgba(230,230,230,0) 75%)}
.hero-caption{position:absolute;left:330px;top:215px;font-size:6px;color:var(--char);font-weight:700;line-height:1.3}
.promo{position:absolute;right:0;top:0;width:260px;height:175px;background:var(--green);padding:14px 16px;color:var(--white)}
.promo h2{font-family:"Oswald",sans-serif;font-weight:600;font-size:17px;line-height:1.12;text-transform:uppercase;color:var(--white)}
.promo p{margin-top:10px;font-family:"Oswald",sans-serif;font-weight:500;font-size:10px;line-height:1.25;text-transform:uppercase;color:var(--char)}
.promo-tag{position:absolute;right:6px;top:48px;background:var(--white);color:var(--green-dark);font-size:6.5px;font-weight:800;padding:2px 6px;transform:rotate(-35deg)}
.signup{display:inline-flex;align-items:center;gap:8px;margin-top:9px;background:var(--black);color:var(--white);font-weight:800;font-size:9px;padding:6px 14px}
.learn{display:flex;align-items:center;gap:5px;margin-top:8px;font-size:7px;font-weight:700;color:var(--white)}
.learn i{width:11px;height:11px;border-radius:50%;background:var(--white)}
.slider-dots{position:absolute;right:16px;bottom:14px;display:flex;gap:5px}
.slider-dots span{width:6px;height:6px;border-radius:50%;background:var(--char)}
.slider-dots span:first-child{background:var(--green)}

/* side info */
.side-info{position:absolute;left:15px;top:560px;width:90px}
.info-box{background:var(--grey);padding:7px;margin-bottom:10px;font-size:6.5px;line-height:1.35;color:var(--char)}
.info-box .icon-row{display:flex;gap:6px;align-items:flex-start}
.phone-number{margin-top:5px;background:var(--black);color:var(--white);font-weight:700;font-size:7.5px;padding:3px 5px;text-align:center}
.card-row{display:flex;gap:3px;margin-top:5px}
.card-row span{width:17px;height:11px;background:var(--char);border-radius:2px}
.card-row span:nth-child(2){background:var(--green)}
.mix-bar{background:var(--black);color:var(--white);font-size:6.5px;font-weight:700;padding:5px 6px;line-height:1.3;text-transform:uppercase}
.warehouse{background:var(--green);padding:8px 7px 10px;color:var(--white)}
.warehouse h3{font-family:"Oswald",sans-serif;font-size:11px;line-height:1.1;text-transform:uppercase;color:var(--black)}
.warehouse ul{margin-top:6px;font-size:6.3px;line-height:1.55}
.warehouse ul li{border-bottom:1px solid rgba(255,255,255,.35)}
.warehouse-pin{background:var(--black);height:28px;display:flex;align-items:center;justify-content:center}

/* popular categories */
.popular{position:absolute;left:105px;top:485px;width:750px}
.popular-head{display:flex;align-items:center;height:40px;padding-left:20px}
.popular-head h2{font-size:15px;font-weight:800;color:var(--black);margin-left:8px}
.popular-head .dot{width:14px;height:14px;border-radius:50%;background:var(--black)}
.wholesale{margin-left:auto;display:flex;gap:6px;align-items:center;font-size:7px;color:var(--char);line-height:1.35;width:170px}
.wholesale b{display:block;font-weight:800;color:var(--black)}
.wholesale .box{width:16px;height:16px;border:2px solid var(--green);flex:none}
.category-grid{display:grid;grid-template-columns:repeat(4,1fr);gap:12px;padding:8px 12px 0 20px}
.category-card{position:relative;height:208px;background:var(--white);border:1px solid var(--grey-mid);box-shadow:0 1px 2px rgba(0,0,0,.08)}
.category-card h3{background:var(--green);color:var(--white);font-size:7.5px;font-weight:800;text-align:center;text-transform:uppercase;padding:5px 0}
.category-card ul{padding:8px 28px 0 10px}
.category-card li{position:relative;padding-left:8px;font-size:6.4px;line-height:1.4;margin-bottom:6px;color:var(--text)}
.category-card li::before{content:"";position:absolute;left:0;top:3px;width:3px;height:3px;background:var(--green)}
.see-more{position:absolute;left:10px;bottom:8px;font-size:6.5px;color:var(--muted)}
.shop-tab{position:absolute;right:0;bottom:0;width:20px;height:92px;background:var(--black);color:var(--white);font-size:7px;font-weight:800;writing-mode:vertical-rl;transform:rotate(180deg);text-align:center;letter-spacing:1px}
.more-card{display:flex;flex-direction:column;align-items:center;justify-content:center;gap:16px;font-size:8px;color:var(--char);font-weight:600;background:var(--grey)}

/* footer */
.site-footer{position:absolute;left:0;top:1000px;width:870px;height:200px;background:var(--black);color:#aaa}
.footer-brand{position:absolute;left:15px;top:16px;display:flex;align-items:center;gap:8px;font-weight:700;font-size:24px;color:var(--white);letter-spacing:-.5px}
.footer-social{position:absolute;right:15px;top:24px;display:flex;gap:6px}
.footer-social span{width:14px;height:14px;border-radius:50%;background:var(--white)}
.footer-rule{position:absolute;left:15px;top:66px;width:840px;height:2px;background:var(--green)}
.footer-cols{position:absolute;left:15px;top:78px;width:840px;display:grid;grid-template-columns:repeat(7,1fr);gap:10px}
.footer-cols h4{font-size:7px;font-weight:800;color:var(--green);text-transform:uppercase;margin-bottom:5px}
.footer-cols li{font-size:6.5px;line-height:1.55}
.copyright{position:absolute;left:0;bottom:10px;width:870px;text-align:center;font-size:6.5px;color:#777}
</style>
</head>
<body>

<header class="site-header">
  <a class="brand" href="#"><span class="brand-mark"></span>Quellmont Haus</a>
  <nav class="main-nav">
    <a href="#">Home</a><a class="active" href="#">Shop</a><a href="#">Blog</a><a href="#">About us</a><a href="#">Vendors</a><a href="#">FAQ</a><a href="#">Contact</a>
  </nav>
  <div class="header-social"><span></span><span></span><span></span></div>
</header>

<div class="tool-bar">
  <div class="shop-all">
    <svg width="9" height="8" viewBox="0 0 9 8"><rect width="9" height="1.5" fill="#8cc63e"/><rect y="3.2" width="9" height="1.5" fill="#8cc63e"/><rect y="6.4" width="9" height="1.5" fill="#8cc63e"/></svg>
    Shop All Categories
  </div>
  <div class="search">
    <div class="search-scope">Search ▾</div>
    <div class="search-input">Enter a product name...</div>
    <div class="search-go">Go</div>
  </div>
  <div class="account-links">My Account &nbsp;|&nbsp; Checkout</div>
  <a class="cart" href="#">
    <svg width="10" height="9" viewBox="0 0 10 9"><path d="M0 1h2l1.5 5h5L10 2.5H3" fill="none" stroke="#fff" stroke-width="1.2"/><circle cx="4" cy="8" r="1" fill="#fff"/><circle cx="8" cy="8" r="1" fill="#fff"/></svg>
    0 items
  </a>
</div>

<ul class="category-menu">
  <li>Vaping Oils</li><li>Batteries</li><li>Cartomizers</li><li>Clearomizers</li><li>Grade oils</li>
  <li>Lorem ipsum</li><li>Product seven</li><li>Product eight</li><li>Product nine</li><li>Product ten</li>
  <li>Product eleven</li><li>Product twelve</li><li>Product thirteen</li><li>Product fourteen</li><li>Product fifteen</li>
</ul>

<section class="hero">
  <div class="hero-visual" role="img" aria-label="Glass and steel clearomizer tank lying on its side"></div>
  <div class="hero-caption">GLASS CLEAROMIZER<br>STEEL BASE</div>
  <div class="promo">
    <span class="promo-tag">EXCLUSIVE</span>
    <h2>All you need about electronic cigarettes at the best prices</h2>
    <p>Register and get free shipping on your order</p>
    <a class="signup" href="#">SIGN UP NOW
      <svg width="8" height="8" viewBox="0 0 8 8"><path d="M1 4h6M4 1l3 3-3 3" fill="none" stroke="#8cc63e" stroke-width="1.5"/></svg>
    </a>
    <div class="learn"><i></i>OR LEARN MORE</div>
  </div>
  <div class="slider-dots"><span></span><span></span><span></span><span></span></div>
</section>

<aside class="side-info">
  <div class="info-box">
    <div class="icon-row">
      <svg width="14" height="14" viewBox="0 0 14 14"><path d="M3 1l2.5 3-1.5 1.5c.8 1.8 2 3 3.5 3.5L9 7.5l3 2.5-1.5 2.5C6 12 2 8 1.5 3z" fill="#111"/></svg>
      <span>You can always place your order by phone<br>9am - 9pm EST</span>
    </div>
    <div class="phone-number">1 800 555 0142</div>
  </div>
  <div class="info-box">
    <div class="icon-row">
      <svg width="14" height="14" viewBox="0 0 14 14"><circle cx="7" cy="7" r="6" fill="none" stroke="#111" stroke-width="1.5"/><path d="M4 7l2 2 4-4" fill="none" stroke="#8cc63e" stroke-width="1.6"/></svg>
      <span>We accept all the major credit cards</span>
    </div>
    <div class="card-row"><span></span><span></span><span></span><span></span></div>
  </div>
  <div class="mix-bar">Enjoy the world first flavor mixing bar</div>
  <div class="warehouse">
    <h3>Visit our warehouse</h3>
    <ul>
      <li>Comfortable couches</li><li>TVs streaming clipora</li><li>Vending machine</li><li>Flavor mixing bar</li><li>No lines for purchase</li><li>VIP cards for regulars</li>
    </ul>
  </div>
  <div class="warehouse-pin">
    <svg width="12" height="16" viewBox="0 0 12 16"><path d="M6 0C2.7 0 0 2.6 0 5.9 0 10 6 16 6 16s6-6 6-10.1C12 2.6 9.3 0 6 0z" fill="#fff"/><circle cx="6" cy="6" r="2.3" fill="#111"/></svg>
  </div>
</aside>

<main class="popular">
  <div class="popular-head">
    <span class="dot"></span>
    <h2>Most Popular Categories</h2>
    <div class="wholesale"><span class="box"></span><span>Wholesale Prices for a Better Purchase<b>FREE DELIVERY</b></span></div>
  </div>
  <div class="category-grid">
    <article class="category-card">
      <h3>Vaping Oils</h3>
      <ul>
        <li>High grade oils made in the USA</li>
        <li>Lowest prices on every blend we carry</li>
        <li>Dozens of flavors ready to mix</li>
        <li>Tested in small fresh batches</li>
      </ul>
      <a class="see-more" href="#">See more ›</a><span class="shop-tab">SHOP NOW</span>
    </article>
    <article class="category-card">
      <h3>Cartomizers</h3>
      <ul>
        <li>Prefilled and empty cartomizers</li>
        <li>Fits most standard battery threads</li>
        <li>Clean draw with steady vapor</li>
        <li>Bulk packs for our regulars</li>
      </ul>
      <a class="see-more" href="#">See more ›</a><span class="shop-tab">SHOP NOW</span>
    </article>
    <article class="category-card">
      <h3>Clearomizers</h3>
      <ul>
        <li>Clear tanks to watch your oil level</li>
        <li>Replaceable coils in every size</li>
        <li>Glass and steel body options</li>
        <li>Easy top fill with no leaking</li>
      </ul>
      <a class="see-more" href="#">See more ›</a><span class="shop-tab">SHOP NOW</span>
    </article>
    <article class="category-card">
      <h3>E-Liquid</h3>
      <ul>
        <li>House blended e-liquid flavors</li>
        <li>Choose your own nicotine level</li>
        <li>Mix your blend at our flavor bar</li>
        <li>Sample sizes for first timers</li>
      </ul>
      <a class="see-more" href="#">See more ›</a><span class="shop-tab">SHOP NOW</span>
    </article>
    <article class="category-card">
      <h3>Batteries</h3>
      <ul>
        <li>Long lasting rechargeable batteries</li>
        <li>Manual and automatic models</li>
        <li>Chargers and adapters in stock</li>
        <li>Full colors to match your kit</li>
      </ul>
      <a class="see-more" href="#">See more ›</a><span class="shop-tab">SHOP NOW</span>
    </article>
    <article class="category-card">
      <h3>Grade Oils</h3>
      <ul>
        <li>Premium grade oils at low prices</li>
        <li>Pure ingredients, no harsh fillers</li>
        <li>Smooth taste from first to last</li>
        <li>Wholesale pricing on large orders</li>
      </ul>
      <a class="see-more" href="#">See more ›</a><span class="shop-tab">SHOP NOW</span>
    </article>
    <article class="category-card">
      <h3>Starter Kits</h3>
      <ul>
        <li>Everything you need to begin</li>
        <li>Battery, tank and charger included</li>
        <li>Simple setup in a few minutes</li>
        <li>Great gift for a new vaper</li>
      </ul>
      <a class="see-more" href="#">See more ›</a><span class="shop-tab">SHOP NOW</span>
    </article>
    <article class="category-card more-card">
      <svg width="44" height="44" viewBox="0 0 44 44"><circle cx="22" cy="22" r="20" fill="none" stroke="#111" stroke-width="3"/><path d="M22 12v20M12 22h20" stroke="#111" stroke-width="3"/></svg>
      More Categories
    </article>
  </div>
</main>

<footer class="site-footer">
  <a class="footer-brand" href="#"><span class="brand-mark"></span>Quellmont Haus</a>
  <div class="footer-social"><span></span><span></span><span></span><span></span></div>
  <div class="footer-rule"></div>
  <div class="footer-cols">
    <div><h4>Location</h4><ul><li>2140 Harlow Ave</li><li>Fenwick, ST 00000</li><li>Open daily</li><li>10am - 10pm</li></ul></div>
    <div><h4>Contact</h4><ul><li>Tel: 1 800 555 0142</li><li>Fax: 1 800 555 0143</li><li>hello@quellmont.example</li></ul></div>
    <div><h4>My Account</h4><ul><li>Login</li><li>Orders &amp; Returns</li><li>VIP Card</li></ul></div>
    <div><h4>Legal</h4><ul><li>Terms</li><li>Privacy</li><li>Age Policy</li></ul></div>
    <div><h4>Help</h4><ul><li>Shipping</li><li>Contact</li><li>FAQ</li></ul></div>
    <div><h4>Links</h4><ul><li>Blog</li><li>Vendors</li><li>Wholesale</li></ul></div>
    <div><h4>Company</h4><ul><li>About us</li><li>Warehouse</li><li>Careers</li></ul></div>
  </div>
  <p class="copyright">Copyright © 2013 Quellmont Haus. All Rights Reserved.</p>
</footer>

</body>
</html>
```